I need the below text put into an illustration/high res image so I can print out and frame and give to my fiance. Can be simple but must look elegant. Idea is that the text can be written in the sand on the attached pics (let me know if you require more high res). Not precious on the dimensions but think no more than 90cm length or width. Can be smaller whatever you think works best. You can half long sentences if you think it will look better.
Update: some of you asked for a picture of us, not sure it works but have attached one
Marriage
Marriage isn’t for you.
You don’t marry to make yourself happy, you marry to make someone else happy.
More than that, your marriage isn’t for yourself, you’re marrying for a family.
Not just for the in-laws and all of that nonsense, but for your future children.
Who do you want to help you raise them?
Who do you want to influence them?
Marriage isn’t for you.
It’s not about you.
Marriage is about the person you married.

```html
<!DOCTYPE html>
<html lang="en">
<head>
<meta charset="UTF-8">
<title>Marriage</title>
<link href="https://fonts.googleapis.com/css2?family=Libre+Caslon+Text:wght@400;700&family=Pinyon+Script&display=swap" rel="stylesheet">
<style>
  :root {
    --sky: #f4f4f4;
    --sky-haze: #e8e8e8;
    --sea-dark: #c4c4c4;
    --sea: #d2d2d2;
    --foam: #e6e6e6;
    --wet-sand: #ececec;
    --sand: #dedede;
    --sand-deep: #d3d3d3;
    --ink: #262626;
    --ink-soft: #3a3a3a;
    --frame-dark: #2c2c2c;
    --frame-light: #ffffff;
    --photo-light: #f0f0f0;
    --photo-mid: #b4b4b4;
    --photo-dark: #4a4a4a;
  }
  html, body {
    margin: 0;
    padding: 0;
    overflow: hidden;
    background: #ffffff;
  }
  .poster {
    position: relative;
    width: 800px;
    height: 1200px;
    overflow: hidden;
    font-family: "Libre Caslon Text", Georgia, serif;
    color: var(--ink);
  }
  .beach-backdrop {
    position: absolute;
    inset: 0;
    background:
      radial-gradient(ellipse 320px 260px at 40px 420px, rgba(248,248,248,0.85), rgba(248,248,248,0) 100%),
      radial-gradient(ellipse 260px 40px at 700px 95px, rgba(150,150,150,0.45), rgba(150,150,150,0) 100%),
      linear-gradient(180deg,
        var(--sky) 0px, var(--sky-haze) 100px,
        var(--sea-dark) 112px, var(--sea) 140px, var(--foam) 165px,
        var(--sea) 190px, var(--foam) 225px,
        var(--wet-sand) 250px, var(--sand) 520px,
        var(--sand-deep) 900px, var(--sand) 1200px);
  }
  .title {
    position: absolute;
    top: 74px;
    left: 0;
    width: 806px;
    margin: 0;
    text-align: center;
    font-family: "Pinyon Script", cursive;
    font-weight: 400;
    font-size: 52px;
    line-height: 60px;
    color: var(--ink);
  }
  .couple-frame {
    position: absolute;
    left: 148px;
    top: 192px;
    width: 506px;
    height: 346px;
  }
  .verse {
    position: absolute;
    left: 70px;
    top: 561px;
    margin: 0;
    font-size: 19.5px;
    line-height: 43.9px;
    color: var(--ink-soft);
  }
  .verse span, .closing span { display: block; white-space: nowrap; }
  .verse strong, .closing strong {
    font-weight: 700;
    color: var(--ink);
  }
  .closing {
    position: absolute;
    right: 66px;
    top: 1005px;
    margin: 0;
    text-align: right;
    font-size: 19.5px;
    line-height: 47px;
    letter-spacing: 1.3px;
    color: var(--ink-soft);
  }
  .rose {
    position: absolute;
    left: 370px;
    top: 1025px;
    width: 140px;
    height: 70px;
    background: radial-gradient(ellipse at 30% 45%, rgba(250,250,250,0.9) 0%, rgba(190,190,190,0.55) 35%, rgba(200,200,200,0) 70%);
  }
</style>
</head>
<body>
<div class="poster">
  <div class="beach-backdrop" role="img" aria-label="Black and white photograph of a beach with waves, wet sand and a distant headland"></div>

  <h1 class="title">Marriage</h1>

  <svg class="couple-frame" viewBox="0 0 506 346" role="img" aria-label="Photograph of the couple embracing">
    <defs>
      <radialGradient id="couplePhotoTone" cx="0.6" cy="0.65" r="0.6">
        <stop offset="0" stop-color="var(--photo-dark)"/>
        <stop offset="0.55" stop-color="var(--photo-mid)"/>
        <stop offset="1" stop-color="var(--photo-light)"/>
      </radialGradient>
      <path id="bracketShape" d="M70,24 Q150,22 215,20 Q240,18 253,6 Q266,18 291,20 Q356,22 436,24 Q446,48 478,52 Q484,90 482,150 Q470,173 482,196 Q484,256 478,294 Q446,298 436,322 Q356,324 291,326 Q266,328 253,340 Q240,328 215,326 Q150,324 70,322 Q60,298 28,294 Q22,256 24,196 Q36,173 24,150 Q22,90 28,52 Q60,48 70,24 Z"/>
    </defs>
    <use href="#bracketShape" fill="url(#couplePhotoTone)" stroke="var(--frame-dark)" stroke-width="10"/>
    <use href="#bracketShape" fill="none" stroke="var(--frame-light)" stroke-width="3"/>
    <use href="#bracketShape" fill="none" stroke="#9a9a9a" stroke-width="1" stroke-dasharray="2 3"
         transform="translate(253 173) scale(0.955) translate(-253 -173)"/>
  </svg>

  <p class="verse">
    <span>Marriage isn’t for you.</span>
    <span><strong>You don’t marry to make yourself happy</strong>,</span>
    <span><strong>you marry to make someone else happy</strong>.</span>
    <span>More than that, your marriage isn’t for yourself,</span>
    <span>you’re marrying for a family.</span>
    <span><strong>Not just for the in–laws and all of that nonsense</strong>,</span>
    <span><strong>but for your future children</strong>.</span>
    <span>Who do you want to help you raise them?</span>
    <span><strong>Who do you want to influence them?</strong></span>
  </p>

  <div class="rose" role="img" aria-label="A single white rose lying on the sand"></div>

  <p class="closing">
    <span>Marriage isn’t for you.</span>
    <span>It’s not about you.</span>
    <span><strong>Marriage is about the person you married</strong>.</span>
  </p>
</div>
</body>
</html>
```